TBV business card

For a business card with our logo

Contact Information for Business Card

Lucien MARVET
Founder & CEO
email : ceo@brightlanternstudio.com / www.brightlanternstudio.com /
instagram / facebook / WhatsApp
N°: +590 690 482 517

Colors

Designer to choose colors to be used in the design.

```html
<!DOCTYPE html>
<html lang="en">
<head>
<meta charset="utf-8">
<title>TBV business card</title>
<link href="https://fonts.googleapis.com/css2?family=Cinzel:wght@600&family=Montserrat:wght@400;500&display=swap" rel="stylesheet">
<style>
  :root {
    --stage: #262626;
    --blue: #1557a6;
    --blue-ink: #1a5bb0;
    --orange: #f47a26;
    --black: #080808;
    --white: #ffffff;
  }
  * { box-sizing: border-box; margin: 0; padding: 0; }
  html, body { width: 1200px; height: 900px; overflow: hidden; background: var(--stage); }
  .canvas { position: relative; width: 1200px; height: 900px; }
  .card { position: absolute; left: 250px; width: 700px; height: 400px; overflow: hidden; }

  /* front */
  .card-front { top: 40px; background: var(--blue); }
  .tile { position: absolute; background: rgba(255,255,255,0.09); }
  .front-mark { position: absolute; left: 50%; top: 135px; transform: translateX(-50%);
    display: flex; align-items: center; gap: 22px; }
  .mark-dot { width: 96px; height: 96px; border-radius: 50%; background: var(--orange); }
  .brand-name { font-family: "Cinzel", serif; font-weight: 600; font-size: 64px; letter-spacing: 6px; line-height: 1; }
  .card-front .brand-name { color: var(--white); }

  /* back */
  .card-back { top: 470px; background: var(--white); }
  .back-top { position: absolute; left: 0; top: 0; width: 100%; height: 230px; background: var(--black);
    border-bottom: 3px solid var(--orange); }
  .back-mark { position: absolute; left: 60px; top: 60px; display: flex; align-items: center; gap: 16px; }
  .back-mark .mark-dot { width: 70px; height: 70px; }
  .back-mark .brand-name { color: var(--blue-ink); font-size: 46px; letter-spacing: 4px; }
  .socials { position: absolute; right: 50px; top: 170px; display: flex; gap: 20px; }
  .social { width: 32px; height: 32px; border-radius: 50%; background: var(--orange); }

  .marker { position: absolute; left: 30px; top: 262px; width: 10px; height: 42px; background: var(--orange); }
  .holder { position: absolute; left: 65px; top: 258px; }
  .holder-name { font-family: "Cinzel", serif; font-weight: 600; font-size: 28px; color: var(--blue-ink); letter-spacing: 1px; }
  .holder-role { font-family: "Montserrat", sans-serif; font-size: 19px; color: var(--orange); margin-top: 2px; }

  .contacts { position: absolute; right: 40px; top: 290px; list-style: none;
    font-family: "Montserrat", sans-serif; font-size: 17px; color: var(--blue-ink); }
  .contacts li { display: flex; justify-content: flex-end; align-items: center; gap: 12px; height: 30px; }
  .contact-icon { width: 20px; display: flex; justify-content: center; color: var(--orange);
    font-weight: 500; font-size: 16px; }
</style>
</head>
<body>
<main class="canvas">
  <section class="card card-front" aria-label="Card front">
    <span class="tile" style="left:190px;top:30px;width:45px;height:30px"></span>
    <span class="tile" style="left:270px;top:40px;width:45px;height:30px"></span>
    <span class="tile" style="left:350px;top:55px;width:55px;height:40px"></span>
    <span class="tile" style="left:195px;top:100px;width:60px;height:45px"></span>
    <span class="tile" style="left:430px;top:110px;width:50px;height:45px"></span>
    <span class="tile" style="left:260px;top:175px;width:55px;height:50px"></span>
    <div class="front-mark">
      <span class="mark-dot"></span>
      <span class="brand-name">TBV</span>
    </div>
  </section>

  <section class="card card-back" aria-label="Card back">
    <div class="back-top">
      <div class="back-mark">
        <span class="mark-dot"></span>
        <span class="brand-name">TBV</span>
      </div>
      <div class="socials" aria-label="Social channels">
        <span class="social"></span>
        <span class="social"></span>
        <span class="social"></span>
      </div>
    </div>
    <span class="marker"></span>
    <div class="holder">
      <p class="holder-name">Lucien MARVET</p>
      <p class="holder-role">Founder &amp; CEO</p>
    </div>
    <ul class="contacts">
      <li>+590 690 482 517<span class="contact-icon">N°</span></li>
      <li>ceo@brightlanternstudio.com
        <span class="contact-icon"><svg width="18" height="14" viewBox="0 0 18 14" fill="none" stroke="#f47a26" stroke-width="1.6"><rect x="1" y="1" width="16" height="12" rx="1.5"/><path d="M1.5 2 9 8l7.5-6"/></svg></span></li>
      <li>www.brightlanternstudio.com
        <span class="contact-icon"><svg width="18" height="18" viewBox="0 0 18 18" fill="none" stroke="#f47a26" stroke-width="1.4"><circle cx="9" cy="9" r="7.5"/><ellipse cx="9" cy="9" rx="3.3" ry="7.5"/><path d="M1.5 9h15M2.8 5h12.4M2.8 13h12.4"/></svg></span></li>
    </ul>
  </section>
</main>
</body>
</html>
```